BRL Design Business Card

I need to develop a business card for my real estate design and investment company. Something clean, classic and professional with a modern vibe.

Industry/Entity Type

Real Estate

Font styles to use
Serif
Sans Serif

```html
<!DOCTYPE html>
<html lang="en">
<head>
<meta charset="utf-8">
<title>BRL Design Business Card</title>
<link href="https://fonts.googleapis.com/css2?family=Open+Sans:wght@300;400;700&display=swap" rel="stylesheet">
<style>
  :root {
    --backdrop: #e6e6e6;
    --card: #ffffff;
    --ink-dark: #333333;
    --accent-grey: #a9a9ab;
    --text-body: #3a3a3a;
    --text-light: #ffffff;
  }
  html, body {
    margin: 0;
    width: 1200px;
    height: 900px;
    overflow: hidden;
    background: var(--backdrop);
    font-family: "Open Sans", Arial, sans-serif;
  }
  .business-card {
    position: absolute;
    left: 150px;
    top: 190px;
    width: 900px;
    height: 520px;
    background: var(--card);
    overflow: hidden;
    box-shadow: 0 18px 40px rgba(0,0,0,0.18);
  }
  .card-shapes {
    position: absolute;
    inset: 0;
  }
  .shape-dark { fill: var(--ink-dark); }
  .shape-grey { fill: var(--accent-grey); }
  .brand {
    position: absolute;
    left: 170px;
    top: 120px;
    color: var(--text-body);
  }
  .brand-name {
    font-weight: 300;
    font-size: 92px;
    letter-spacing: 10px;
    line-height: 1;
    margin: 0;
  }
  .brand-tagline {
    font-weight: 300;
    font-size: 19px;
    margin: 10px 0 0 6px;
    letter-spacing: 0.5px;
  }
  .contact-list {
    position: absolute;
    left: 290px;
    top: 300px;
    margin: 0;
    padding: 0;
    list-style: none;
    font-size: 15px;
    color: var(--text-body);
    line-height: 21px;
  }
  .contact-list li {
    display: flex;
    align-items: flex-start;
    gap: 8px;
  }
  .contact-icon {
    flex: none;
    width: 14px;
    height: 14px;
    margin-top: 4px;
  }
  .contact-icon circle { fill: var(--ink-dark); }
  .contact-icon path, .contact-icon rect { fill: var(--card); }
  .owner {
    position: absolute;
    right: 48px;
    top: 70px;
    text-align: right;
    color: var(--text-light);
  }
  .owner-name {
    margin: 0;
    font-weight: 700;
    font-size: 30px;
  }
  .owner-role {
    margin: 2px 0 0;
    font-weight: 400;
    font-size: 24px;
  }
</style>
</head>
<body>
  <article class="business-card">
    <svg class="card-shapes" width="900" height="520" viewBox="0 0 900 520" aria-hidden="true">
      <path class="shape-grey" d="M0 120 C40 260 150 430 330 520 L300 520 C120 440 20 300 0 150 Z"/>
      <path class="shape-dark" d="M0 150 C20 300 120 440 300 520 L0 520 Z"/>
      <path class="shape-grey" d="M650 0 C590 110 600 230 560 330 C530 410 480 480 440 520 L470 520 C520 470 560 410 590 330 C630 230 620 110 680 0 Z"/>
      <path class="shape-dark" d="M680 0 C620 110 630 230 590 330 C560 410 520 470 470 520 L900 520 L900 0 Z"/>
    </svg>

    <header class="brand">
      <h1 class="brand-name">BRL</h1>
      <p class="brand-tagline">Design and Investments</p>
    </header>

    <ul class="contact-list">
      <li>
        <svg class="contact-icon" viewBox="0 0 14 14" aria-hidden="true"><circle cx="7" cy="7" r="7"/><path d="M7 3a2.5 2.5 0 0 1 2.5 2.5C9.5 7.5 7 11 7 11S4.5 7.5 4.5 5.5A2.5 2.5 0 0 1 7 3Z"/></svg>
        <span>Suite # 410, Park Bldg,<br>NY 10016</span>
      </li>
      <li>
        <svg class="contact-icon" viewBox="0 0 14 14" aria-hidden="true"><circle cx="7" cy="7" r="7"/><path d="M4 3.5 5.6 3l1 2-1 .8a5 5 0 0 0 2.6 2.6l.8-1 2 1-.5 1.6C8 10.5 3.5 6 4 3.5Z"/></svg>
        <span>555-201-4410</span>
      </li>
      <li>
        <svg class="contact-icon" viewBox="0 0 14 14" aria-hidden="true"><circle cx="7" cy="7" r="7"/><rect x="4" y="4.5" width="6" height="5" rx="0.5"/></svg>
        <span>555-318-2096</span>
      </li>
      <li>
        <svg class="contact-icon" viewBox="0 0 14 14" aria-hidden="true"><circle cx="7" cy="7" r="7"/><rect x="5" y="3" width="4" height="8" rx="0.8"/></svg>
        <span>555-472-6631</span>
      </li>
      <li>
        <svg class="contact-icon" viewBox="0 0 14 14" aria-hidden="true"><circle cx="7" cy="7" r="7"/><path d="M3.5 4.5h7v5h-7Zm.8.6L7 7.2l2.7-2.1Z"/></svg>
        <span>hello@brlstudio.com</span>
      </li>
      <li>
        <svg class="contact-icon" viewBox="0 0 14 14" aria-hidden="true"><circle cx="7" cy="7" r="7"/><path d="M7 3.2a3.8 3.8 0 1 1 0 7.6 3.8 3.8 0 0 1 0-7.6Zm0 .9a2.9 2.9 0 1 0 0 5.8 2.9 2.9 0 0 0 0-5.8Z"/></svg>
        <span>www.brlstudio.com</span>
      </li>
    </ul>

    <section class="owner">
      <h2 class="owner-name">Daniel Rowe</h2>
      <p class="owner-role">Owner / C.E.O</p>
    </section>
  </article>
</body>
</html>
```